Webdesign für Software Ingenieurbüro
Vielen Dank für das professionelle Design, Umsetzung mit WordPress und rasche Reaktionszeiten. MondscheinKobold geht die Extrameile.
Zielgruppe
English text below
Meine Firma erstellt Software und bietet sämtliche Dienstleistungen rund um die Softwareentwicklung an.
Die Zielgruppe sind Auftraggeber, welche Software-Engineering/Entwicklungsaufträge vergeben.
English
My company creates software and offers all services related to software development.
The target group are those who award software engineering / development contracts.
Aufgabenstellung
Die bestehende Seite www.tarnvok-systems.ch soll neu und modern designed werden. Die Struktur der Seite (Menuunterteilung) kann (muss aber nicht zwingend) übernommen werden.
Das Logo kann, muss aber nicht übernommen werden.
Ev. als OnePage-Seite gestalten.
Responsive-Design ist zwingend, d.h. die Seite muss sowohl auf dem Desktop wie auch auf dem Mobile-Gerät ansprechend aussehen.
Zur Illustration soll auf Fotos verzichtet werden. Aber es können sehr gerne Vektorgrafiken für die Illustration und/oder Icons verwendet werden.
Link auf Social-Media Qorvu muss vorhanden sein.
Der persönliche Kontakt zum Kunden ist mir wichtig, deshalb sollte mein Foto vorhanden sein. Ev. nicht so prominent wie auf der aktuellen Seite.
Die Umsetzung wird mit Wordpress und einem Standard-Theme geschehen. Falls Sie Wordpress kennen, können Sie das Theme angeben, mit welchem sich die Seite umsetzen lässt.
The existing site www.tarnvok-systems.ch is to be redesigned and modernized. The structure of the page (menu subdivision) can (but does not have to be) mandatory.
The logo can, but does not have to be adopted.
Ev. as a OnePage page.
Responsive design is required, the page must look appealing both on the desktop and on the mobile device.
For the illustration, photographs are not desired. But vector graphics can be used for illustration and / or icons.
Link to social media Qorvu must be available.
Personal contact with the customer is important to me, so my photo should be available. Ev. not as prominent as on the current page.
The implementation will be done with Wordpress and a standard theme. If you are familiar with Wordpress, you can specify the theme with which the page can be implemented.

```html
<!DOCTYPE html>
<html lang="de">
<head>
<meta charset="utf-8">
<title>Tarnvok Systems – Professionelle Softwareentwicklung</title>
<link href="https://fonts.googleapis.com/css2?family=Roboto:ital,wght@1,400;1,900&family=Source+Sans+3:wght@400;600&family=Exo+2:wght@800&display=swap" rel="stylesheet">
<style>
:root{
  --blue-dark:#0b3f94;
  --blue:#1565c0;
  --blue-bright:#3d7fe0;
  --accent:#1e6fcf;
  --ink:#3b3b3b;
  --ink-soft:#5a5a5a;
  --white:#ffffff;
  --screen:#f1f4f8;
  --frame:#f8f9fa;
  --footer:#0a1230;
}
*{margin:0;padding:0;box-sizing:border-box}
html,body{width:841px;height:1200px;overflow:hidden}
body{position:relative;background:var(--white);font-family:"Source Sans 3",sans-serif;color:var(--ink)}
.abs{position:absolute}
.center{left:0;width:841px;text-align:center}

.hero{top:0;left:0;width:841px;height:305px;background:linear-gradient(90deg,#0c3c8f 0%,#1455b0 55%,#1a6ac8 100%)}
.brand{left:56px;top:15px;color:var(--white);font-weight:600;font-size:11px;line-height:12px;display:flex;align-items:center;gap:5px}
.brand .mark{width:13px;height:13px;border:1.5px solid var(--white);border-radius:50%}
.nav-item{top:23px;font-size:7.5px;line-height:10px;color:var(--white)}
.nav-item.active{border-bottom:1px solid #8fc0ff;padding:0 2px 3px}
.social-top{top:24px;left:735px;font-size:6px;color:var(--white);display:flex;gap:6px}
.hero-title{top:96px;font-family:"Roboto",sans-serif;font-style:italic;font-weight:400;font-size:19px;line-height:22px;color:var(--white)}
.hero-title b,.title b{font-weight:900}
.hero-text{top:135px;font-size:8px;line-height:11.5px;color:#dbe7ff}
.btn{display:flex;align-items:center;justify-content:center;border-radius:11px;background:linear-gradient(90deg,#3573d6,#4b92f0);color:var(--white);font-family:"Roboto",sans-serif;font-size:7px;letter-spacing:.1px;box-shadow:0 3px 6px rgba(30,90,200,.35)}

.stats{left:157px;top:249px;width:527px;height:81px;background:var(--white);border:1px solid #dde3ea;border-radius:3px;box-shadow:0 2px 4px rgba(0,0,0,.06);display:flex}
.stat{flex:1;text-align:center;padding-top:14px}
.stat .num{font-family:"Exo 2",sans-serif;font-weight:800;font-size:33px;line-height:32px;color:var(--accent)}
.stat .lbl{font-size:12.5px;color:var(--ink-soft);margin-top:1px}
.divider{top:267px;width:1px;height:45px;background:#4a86dc}
.divider::after{content:"";position:absolute;left:-2px;top:20px;width:5px;height:5px;border-radius:50%;background:#4a86dc}

.title{font-family:"Roboto",sans-serif;font-style:italic;font-weight:400;font-size:18px;color:var(--ink);line-height:18px}
.rule{height:1px;width:32px;left:404px;background:#5b8fd6}
.method{top:442px;width:100px;text-align:center;font-size:10.5px;line-height:12.5px;color:var(--ink)}
.method svg,.method .owl{display:block;margin:0 auto 21px;width:44px;height:44px}
.method .owl{width:30px;border-radius:6px;background:linear-gradient(160deg,#d5e4fb,#a9c6f2)}

.tablet{left:165px;top:639px;width:512px;height:300px;background:var(--frame);border:1px solid #e1e4e8;border-radius:16px;box-shadow:0 -2px 12px rgba(0,0,0,.05)}
.screen{left:207px;top:678px;width:425px;height:260px;background:var(--screen);border:1px solid #dfe4ea}
.home-btn{left:182px;top:831px;width:12px;height:12px;border-radius:50%;background:#f0f1f3;border:1px solid #e6e8eb}
.cam{left:653px;top:835px;width:5px;height:5px;border-radius:50%;background:#8b95a3}
.tech{width:84px;text-align:center;font-size:9px;font-weight:600;margin-left:-42px}

.contact{left:0;top:919px;width:841px;height:252px;background:linear-gradient(160deg,#0d43a0 0%,#0e3d93 50%,#0a2f80 100%)}
.contact-text{left:225px;top:1008px;width:165px;font-size:7.5px;line-height:10.5px;color:#dce6fb}
.contact-text p{margin-bottom:6px}
.profile{left:226px;top:1096px;font-family:"Roboto",sans-serif;font-style:italic;font-size:7.5px;color:var(--white)}
.social-bottom{left:226px;top:1117px;font-size:6px;color:var(--white);display:flex;gap:6px}
.field{left:455px;width:161px;border-bottom:1px solid #6f9bf0;font-size:8px;color:var(--white);height:12px;line-height:12px}
.field-lbl{left:455px;font-size:4.5px;color:#b6c9f3;letter-spacing:.2px}
.footer{left:0;top:1171px;width:841px;height:29px;background:var(--footer);color:#d5dbe8;font-size:6px;text-align:center;line-height:29px}
</style>
</head>
<body>

<header class="abs hero" role="img" aria-label="Blauer Hintergrund mit dezentem Muster aus Technik-Symbolen"></header>
<div class="abs brand"><span class="mark"></span>Tarnvok Systems</div>
<nav>
  <span class="abs nav-item active" style="left:494px">Home</span>
  <span class="abs nav-item" style="left:541px">Dienstleistungen</span>
  <span class="abs nav-item" style="left:621px">Firma</span>
  <span class="abs nav-item" style="left:665px">Kontakt</span>
  <span class="abs nav-item" style="left:715px">|</span>
</nav>
<div class="abs social-top"><span>Linkora</span><span>Qorvu</span><span>Facelane</span></div>
<h1 class="abs center hero-title">Professionelle <b>Softwareentwicklung</b></h1>
<p class="abs center hero-text">Tarnvok Systems stellt unter Verwendung modernster Technologien und leichtgewichtiger<br>Prozessen qualitativ hochstehende Software her.</p>
<div class="abs btn" style="left:359px;top:186px;width:122px;height:20px">HABEN SIE EIN PROJEKT?</div>

<section class="abs stats">
  <div class="stat"><div class="num">18</div><div class="lbl">Jahre Erfahrung</div></div>
  <div class="stat"><div class="num">232</div><div class="lbl">zufriedene Kunden</div></div>
  <div class="stat"><div class="num">15</div><div class="lbl">Coaching-Projekte</div></div>
</section>
<div class="abs divider" style="left:332px"></div>
<div class="abs divider" style="left:508px"></div>

<h2 class="abs center title" style="top:383px">Unsere <b>Methodik</b></h2>
<div class="abs rule" style="top:420px"></div>

<div class="abs method" style="left:173px"><div class="owl" role="img" aria-label="Linien-Illustration einer Eule"></div>Teamführung und Coaching</div>
<div class="abs method" style="left:304px">
  <svg viewBox="0 0 46 46" fill="none" stroke="#3d7fe0" stroke-width="1.6"><circle cx="26" cy="25" r="16"/><path d="M22 5h8M26 5v4M38 12l3-3M26 25l6-8M2 20h10M4 26h8M6 32h8"/></svg>
  Scrum und Extreme Programming</div>
<div class="abs method" style="left:431px;width:110px">
  <svg viewBox="0 0 46 46" fill="none" stroke="#3d7fe0" stroke-width="1.6"><rect x="2" y="4" width="40" height="29" rx="2"/><path d="M2 27h28M16 33v6M10 40h16"/><rect x="26" y="20" width="12" height="22" rx="2"/></svg>
  Continuous Integration/ Delivery</div>
<div class="abs method" style="left:566px">
  <svg viewBox="0 0 46 46" fill="none" stroke="#3d7fe0" stroke-width="1.6"><path d="M21 8v32M12 42h20M15 38h12M5 12l16-3 18-3M9 12l-6 12h12zM39 6l-6 12h12z"/><path d="M3 24a6 4 0 0 0 12 0M33 18a6 4 0 0 0 12 0"/></svg>
  Application Lifecylce Management</div>

<div class="abs btn" style="left:371px;top:562px;width:99px;height:20px">LASS UNS START</div>

<div class="abs tablet"></div>
<div class="abs home-btn"></div>
<div class="abs cam"></div>
<div class="abs screen"></div>
<h2 class="abs center title" style="top:712px"><b>Konzentrieren</b> Sie sich<br>auf <b>Technologie</b></h2>
<div class="abs rule" style="top:772px"></div>
<p class="abs center" style="top:792px;font-size:8.5px;line-height:10.5px;color:var(--ink-soft);padding-left:14px">Über 18 Jahre Erfahrung in der Softwareentwicklung und Entwicklung von<br>Backendsystemen mit hohem Transaktionsaufkommen</p>

<div class="abs tech" style="left:274px;top:846px;color:#e2231a">Kavra</div>
<div class="abs tech" style="left:372px;top:846px;color:#333">Quelldat Server</div>
<div class="abs tech" style="left:468px;top:846px;color:#6db33f">Sprossa</div>
<div class="abs tech" style="left:565px;top:846px;color:#444">Winkelio</div>
<div class="abs tech" style="left:274px;top:874px;color:#e2231a">Orvane</div>
<div class="abs tech" style="left:372px;top:872px;color:#1a1ad6;font-size:12px">&lt;xml /&gt;</div>
<div class="abs tech" style="left:468px;top:874px;color:#555">Ruhevar</div>
<div class="abs tech" style="left:565px;top:874px;color:#5da839">Schaumio</div>

<section class="abs contact"></section>
<h2 class="abs center title" style="top:951px;color:var(--white)">Sie können eine <b>Frage stellen</b></h2>
<div class="abs rule" style="top:991px"></div>
<div class="abs contact-text">
  <p>Tarnvok Systems GmbH fokussiert sich auf die professionelle Softwareentwicklung .</p>
  <p>Ich freue mich auf Ihre Nachricht. Füllen Sie bitte untenstehendes Formular aus. Ich werde so rasch wie möglich mit Ihnen in Kontakt treten.</p>
</div>
<div class="abs profile">Besuchen Sie mein Profil: &nbsp;<b>Bernhard Kolmer</b></div>
<div class="abs social-bottom"><span>Linkora</span><span>Qorvu</span><span>Facelane</span></div>

<div class="abs field" style="top:1010px">Alex|</div>
<div class="abs field-lbl" style="top:1026px">NAME</div>
<div class="abs field" style="top:1040px"></div>
<div class="abs field-lbl" style="top:1056px">E-MAIL</div>
<div class="abs field" style="top:1070px"></div>
<div class="abs field-lbl" style="top:1088px">NACHRICHT</div>
<div class="abs btn" style="left:479px;top:1112px;width:114px;height:20px">SCHICKEN &nbsp;NACHRICHT</div>

<footer class="abs footer">© Copyright 2010 - 2017 Tarnvok Systems GmbH. All rights reserved.</footer>
</body>
</html>
```